Electrical Safety Inspection for High End Customers

Flyer designed to advertise a 50 point electrical safety check service available from a recent start up electrician's firm in Auckland, New Zealand. I am a registered electrical inspector with 16 years experience.
Targeting high end customers, so I want the flyer to have a premium feel to it (glossy black background, etc). The final design should communicate peace of mind. The price will be $60 incl. GST
The checks included should be 1) Mains Cable 2)Mains entry point 3)Switchboard 4)Circuit protection correctly rated 5)Circuit protection operational 6)The main earthing system 7)Safety systems 8)Light fittings 9)Socket outlets 10)Deterioration of fittings 11)Deterioration of cabling 12)Compliance with current regulations
I have included a copy of the test sheet for reference. I have also included my logo and the qualified wiremen's guild of Ostravel, both of which must be present.
Target Market(s)
High end home owners
Industry/Entity Type
Electrician
Colors
Designer to choose colors to be used in the design.
Look and feel

```html
<!DOCTYPE html>
<html lang="en">
<head>
<meta charset="utf-8">
<title>Volt Crest Electrical – 50 Point Electrical Safety Check</title>
<link href="https://fonts.googleapis.com/css2?family=Anton&family=Montserrat:wght@500;600;700;800&family=Roboto:wght@500&family=Roboto+Condensed:wght@700&display=swap" rel="stylesheet">
<style>
  :root {
    --red: #e8202a;
    --blue: #1b75c0;
    --black: #0b0b0c;
    --ink: #111111;
    --white: #ffffff;
    --rule: #9a9a9a;
    --dark-top: #1a1512;
    --dark-bottom: #050506;
  }
  * { margin: 0; padding: 0; box-sizing: border-box; }
  html, body { width: 968px; height: 1200px; overflow: hidden; background: var(--white); }
  .flyer { position: relative; width: 968px; height: 1200px; background: var(--white); overflow: hidden; font-family: "Montserrat", sans-serif; }

  .brand { position: absolute; left: 66px; top: 52px; display: flex; align-items: center; gap: 12px; }
  .brand-dot { width: 52px; height: 52px; border-radius: 50%; background: var(--black); }
  .brand-name { font-family: "Montserrat", sans-serif; font-weight: 800; font-size: 29px; line-height: 1; color: var(--ink); letter-spacing: 1px; }

  .headline { position: absolute; left: 500px; top: 40px; width: 450px; height: 110px; }
  .headline-fifty { position: absolute; left: 0; top: -12px; font-family: "Anton", sans-serif; font-size: 118px; line-height: 1; color: var(--ink); letter-spacing: -2px; }
  .headline-tick { position: absolute; left: 98px; top: -6px; width: 115px; height: 90px; }
  .headline-point { position: absolute; left: 232px; top: 0; font-family: "Anton", sans-serif; font-size: 92px; line-height: 1; color: var(--ink); transform: scaleY(1.12); transform-origin: top left; }

  .service-title { position: absolute; left: 513px; top: 160px; width: 318px; border-top: 1px solid var(--rule); border-bottom: 1px solid var(--rule); padding: 4px 0 6px; text-align: center; }
  .service-title h1 { font-family: "Anton", sans-serif; font-weight: 400; color: var(--red); font-size: 46px; line-height: 54px; letter-spacing: -0.5px; }
  .service-area { position: absolute; left: 500px; top: 293px; width: 344px; text-align: center; font-weight: 800; font-size: 19px; color: var(--ink); }

  .dark-field { position: absolute; left: 0; top: 506px; width: 968px; height: 530px; background: linear-gradient(160deg, var(--dark-top), var(--dark-bottom) 60%); }
  .credentials { position: absolute; left: 520px; top: 343px; width: 448px; height: 163px; background: var(--blue); }
  .credentials ul { list-style: none; position: absolute; left: 93px; top: 18px; color: var(--white); font-weight: 500; font-size: 16.5px; line-height: 19px; }
  .credentials li { position: relative; margin-bottom: 12px; letter-spacing: 0.3px; }
  .credentials li::before { content: ""; position: absolute; left: -23px; top: 4px; width: 10px; height: 10px; border-radius: 50%; background: var(--white); }

  .hero-frame { position: absolute; left: 0; top: 0; width: 968px; height: 1036px; }

  .checks-tab { position: absolute; left: 49px; top: 723px; width: 325px; height: 37px; background: var(--blue); clip-path: polygon(0 0, 100% 0, 93% 100%, 0 100%); color: var(--white); font-weight: 800; font-size: 20px; line-height: 37px; padding-left: 14px; letter-spacing: 0.3px; }
  .checks-list { position: absolute; top: 779px; list-style: none; font-family: "Roboto", sans-serif; font-weight: 500; font-size: 15.5px; line-height: 16.5px; color: var(--white); }
  .checks-list.col-a { left: 55px; }
  .checks-list.col-b { left: 291px; }
  .checks-list li { position: relative; padding-left: 20px; height: 16.5px; margin-bottom: 14px; white-space: nowrap; }
  .checks-list li.two-line { height: 33px; margin-bottom: 14px; }
  .check-icon { position: absolute; left: 0; top: 1px; width: 14px; height: 14px; }

  .price { position: absolute; left: 760px; top: 950px; width: 175px; text-align: center; color: var(--white); }
  .price-amount { font-weight: 500; font-size: 31px; line-height: 34px; }
  .price-note { font-weight: 500; font-size: 12.5px; letter-spacing: 0.5px; }

  .tagline { position: absolute; left: 0; top: 1036px; width: 968px; height: 35px; background: var(--blue); color: var(--white); text-align: center; font-weight: 800; font-size: 18.5px; line-height: 35px; letter-spacing: 0.3px; }

  .cta { position: absolute; left: 33px; top: 1072px; width: 145px; height: 100px; background: var(--red); color: var(--white); text-align: center; font-weight: 500; font-size: 17.5px; line-height: 19.5px; padding-top: 12px; }

  .contact { position: absolute; left: 231px; top: 1088px; }
  .contact-icon { position: absolute; left: 0; width: 40px; height: 40px; }
  .contact-phone { position: absolute; left: 47px; top: -2px; font-family: "Roboto Condensed", sans-serif; font-weight: 700; font-size: 35px; line-height: 40px; color: #2a2a2a; white-space: nowrap; letter-spacing: -0.3px; }
  .contact-web { position: absolute; left: 89px; top: 1139px; font-weight: 700; font-size: 12.3px; line-height: 18px; color: #2a2a2a; }

  .divider { position: absolute; top: 1103px; width: 1px; height: 58px; background: var(--rule); }

  .social { position: absolute; left: 555px; top: 1098px; width: 118px; text-align: center; }
  .social-label { font-weight: 500; font-size: 10.5px; line-height: 12px; color: #333; letter-spacing: 0.3px; }
  .social-dots { display: flex; justify-content: center; gap: 6px; margin-top: 11px; }
  .social-dots span { width: 25px; height: 25px; border-radius: 50%; background: var(--ink); }

  .guild-badge { position: absolute; left: 720px; top: 1114px; width: 140px; height: 46px; background: var(--blue); border-radius: 3px; }
  .inspector-badge { position: absolute; left: 880px; top: 1113px; width: 48px; height: 48px; border-radius: 50%; border: 3px solid var(--ink); }
</style>
</head>
<body>
<main class="flyer">

  <div class="brand">
    <span class="brand-dot"></span>
    <span class="brand-name">VOLT CREST<br><span style="font-size:15px;letter-spacing:4px;">ELECTRICAL</span></span>
  </div>

  <div class="headline">
    <span class="headline-fifty">50</span>
    <svg class="headline-tick" viewBox="0 0 115 90" aria-hidden="true">
      <path d="M12 48 L40 78 L110 4" fill="none" stroke="#e8202a" stroke-width="12" stroke-linecap="round" stroke-linejoin="round"/>
    </svg>
    <span class="headline-point">POINT</span>
  </div>

  <div class="service-title">
    <h1>ELECTRICAL SAFETY<br>CHECK SERVICE</h1>
  </div>
  <p class="service-area">AVAILABLE IN YOUR CITY</p>

  <div class="dark-field" role="img" aria-label="Dimmed photograph of switchboard wiring behind the content"></div>

  <section class="credentials">
    <ul>
      <li>16 YEARS EXPERIENCE</li>
      <li>FULLY REGISTERED<br>ELECTRICAL INSPECTOR</li>
      <li>PROFESSIONALISM,<br>EXPERTISE AND EFFICIENCY</li>
    </ul>
  </section>

  <svg class="hero-frame" viewBox="0 0 968 1036" aria-hidden="false">
    <defs>
      <linearGradient id="switchboardTone" x1="0" y1="0" x2="1" y2="1">
        <stop offset="0" stop-color="#d8cfc6"/>
        <stop offset="0.45" stop-color="#a7554a"/>
        <stop offset="1" stop-color="#2f3b66"/>
      </linearGradient>
      <linearGradient id="wiringTone" x1="0" y1="0" x2="1" y2="1">
        <stop offset="0" stop-color="#c9c2b8"/>
        <stop offset="1" stop-color="#c4473e"/>
      </linearGradient>
      <linearGradient id="planTone" x1="0" y1="0" x2="1" y2="1">
        <stop offset="0" stop-color="#8a6a4c"/>
        <stop offset="1" stop-color="#e8e6e2"/>
      </linearGradient>
      <linearGradient id="workerTone" x1="0" y1="0" x2="1" y2="1">
        <stop offset="0" stop-color="#7d6a5e"/>
        <stop offset="1" stop-color="#e2a46f"/>
      </linearGradient>
    </defs>

    <polygon class="hero-red" points="96,146 404,146 560,409 404,679 96,679 -60,409" fill="#e8202a" stroke="#e8202a" stroke-width="22" stroke-linejoin="round"/>
    <polygon class="hero-photo" role="img" aria-label="Photo of an electrician testing a switchboard with a multimeter" points="98,168 402,168 540,412 402,657 98,657 -48,412" fill="url(#switchboardTone)" stroke="#ffffff" stroke-width="2" stroke-linejoin="round"/>

    <g class="hex-gallery">
      <polygon points="496,641 563,528 697,528 764,641 697,754 563,754" fill="none" stroke="#ffffff" stroke-width="3" stroke-linejoin="round"/>
      <polygon role="img" aria-label="Photo of gloved hands connecting wires at a wall outlet" points="512,641 571,542 689,542 748,641 689,740 571,740" fill="url(#wiringTone)"/>

      <polygon points="713,767 780,654 914,654 981,767 914,880 780,880" fill="none" stroke="#ffffff" stroke-width="3" stroke-linejoin="round"/>
      <polygon role="img" aria-label="Photo of hands reviewing wiring plans on a workbench" points="729,767 788,668 906,668 965,767 906,866 788,866" fill="url(#planTone)"/>

      <polygon points="496,893 563,780 697,780 764,893 697,1006 563,1006" fill="none" stroke="#ffffff" stroke-width="3" stroke-linejoin="round"/>
      <polygon role="img" aria-label="Photo of an electrician in a hard hat working overhead" points="512,893 571,794 689,794 748,893 689,992 571,992" fill="url(#workerTone)"/>
    </g>
  </svg>

  <h2 class="checks-tab">CHECKS INCLUDED</h2>

  <ul class="checks-list col-a">
    <li><svg class="check-icon" viewBox="0 0 14 14"><circle cx="7" cy="7" r="6" fill="none" stroke="#1b75c0" stroke-width="2"/><path d="M4 7.2 L6.2 9.3 L10 5" fill="none" stroke="#fff" stroke-width="1.6"/></svg>MAINS CABLE</li>
    <li><svg class="check-icon" viewBox="0 0 14 14"><circle cx="7" cy="7" r="6" fill="none" stroke="#1b75c0" stroke-width="2"/><path d="M4 7.2 L6.2 9.3 L10 5" fill="none" stroke="#fff" stroke-width="1.6"/></svg>MAINS ENTRY POINT</li>
    <li><svg class="check-icon" viewBox="0 0 14 14"><circle cx="7" cy="7" r="6" fill="none" stroke="#1b75c0" stroke-width="2"/><path d="M4 7.2 L6.2 9.3 L10 5" fill="none" stroke="#fff" stroke-width="1.6"/></svg>SWITCHBOARD</li>
    <li class="two-line"><svg class="check-icon" viewBox="0 0 14 14"><circle cx="7" cy="7" r="6" fill="none" stroke="#1b75c0" stroke-width="2"/><path d="M4 7.2 L6.2 9.3 L10 5" fill="none" stroke="#fff" stroke-width="1.6"/></svg>CIRCUIT PROTECTION<br>CORRECTLY RATED</li>
    <li class="two-line"><svg class="check-icon" viewBox="0 0 14 14"><circle cx="7" cy="7" r="6" fill="none" stroke="#1b75c0" stroke-width="2"/><path d="M4 7.2 L6.2 9.3 L10 5" fill="none" stroke="#fff" stroke-width="1.6"/></svg>CIRCUIT PROTECTION<br>OPERATIONAL</li>
    <li class="two-line"><svg class="check-icon" viewBox="0 0 14 14"><circle cx="7" cy="7" r="6" fill="none" stroke="#1b75c0" stroke-width="2"/><path d="M4 7.2 L6.2 9.3 L10 5" fill="none" stroke="#fff" stroke-width="1.6"/></svg>THE MAIN EARTHING<br>SYSTEM</li>
  </ul>

  <ul class="checks-list col-b">
    <li><svg class="check-icon" viewBox="0 0 14 14"><circle cx="7" cy="7" r="6" fill="none" stroke="#1b75c0" stroke-width="2"/><path d="M4 7.2 L6.2 9.3 L10 5" fill="none" stroke="#fff" stroke-width="1.6"/></svg>SAFETY SYSTEMS</li>
    <li><svg class="check-icon" viewBox="0 0 14 14"><circle cx="7" cy="7" r="6" fill="none" stroke="#1b75c0" stroke-width="2"/><path d="M4 7.2 L6.2 9.3 L10 5" fill="none" stroke="#fff" stroke-width="1.6"/></svg>LIGHT FITTINGS</li>
    <li><svg class="check-icon" viewBox="0 0 14 14"><circle cx="7" cy="7" r="6" fill="none" stroke="#1b75c0" stroke-width="2"/><path d="M4 7.2 L6.2 9.3 L10 5" fill="none" stroke="#fff" stroke-width="1.6"/></svg>SOCKET OUTLETS</li>
    <li class="two-line"><svg class="check-icon" viewBox="0 0 14 14"><circle cx="7" cy="7" r="6" fill="none" stroke="#1b75c0" stroke-width="2"/><path d="M4 7.2 L6.2 9.3 L10 5" fill="none" stroke="#fff" stroke-width="1.6"/></svg>DETERIORATION OF<br>FITTINGS</li>
    <li class="two-line"><svg class="check-icon" viewBox="0 0 14 14"><circle cx="7" cy="7" r="6" fill="none" stroke="#1b75c0" stroke-width="2"/><path d="M4 7.2 L6.2 9.3 L10 5" fill="none" stroke="#fff" stroke-width="1.6"/></svg>DETERIORATION OF<br>CABLING</li>
    <li class="two-line"><svg class="check-icon" viewBox="0 0 14 14"><circle cx="7" cy="7" r="6" fill="none" stroke="#1b75c0" stroke-width="2"/><path d="M4 7.2 L6.2 9.3 L10 5" fill="none" stroke="#fff" stroke-width="1.6"/></svg>COMPLIANCE WITH<br>CURRENT REGULATIONS</li>
  </ul>

  <div class="price">
    <p class="price-amount">$60 GST</p>
    <p class="price-note">INCLUDED</p>
  </div>

  <p class="tagline">LEADERS IN&nbsp; ELECTRICAL DESIGN AND INSTALLATION</p>

  <p class="cta">FOR MORE<br>INSPECTIONS<br>CALL OR VISIT</p>

  <div class="contact">
    <svg class="contact-icon" style="top:2px" viewBox="0 0 40 40" aria-hidden="true">
      <circle cx="20" cy="20" r="19" fill="#e8202a"/>
      <path d="M13 10 L17 10 L18.5 15 L16 17 C17.5 20.5 19.5 22.5 23 24 L25 21.5 L30 23 L30 27 C30 28.5 28.5 30 27 30 C18 29 11 22 10 13 C10 11.5 11.5 10 13 10 Z" fill="none" stroke="#fff" stroke-width="2" stroke-linejoin="round"/>
    </svg>
    <p class="contact-phone">64 027 555 0142</p>
    <svg class="contact-icon" style="top:50px" viewBox="0 0 40 40" aria-hidden="true">
      <circle cx="20" cy="20" r="19" fill="#e8202a"/>
      <circle cx="20" cy="20" r="10" fill="none" stroke="#fff" stroke-width="2"/>
      <ellipse cx="20" cy="20" rx="4.5" ry="10" fill="none" stroke="#fff" stroke-width="2"/>
      <path d="M10 20 H30 M12 15 H28 M12 25 H28" stroke="#fff" stroke-width="1.6"/>
    </svg>
  </div>
  <p class="contact-web" style="left:320px;">www.voltcrestelectrical.co.nz<br>hello@voltcrestelectrical.co.nz</p>

  <span class="divider" style="left:527px"></span>

  <div class="social">
    <p class="social-label">GET SOCIAL<br>WITH US</p>
    <div class="social-dots" aria-label="Social media links">
      <span></span><span></span><span></span>
    </div>
  </div>

  <span class="divider" style="left:697px"></span>

  <div class="guild-badge" role="img" aria-label="Member badge: qualified wiremen's guild of Ostravel"></div>
  <div class="inspector-badge" role="img" aria-label="Electrical inspectors' association badge"></div>

</main>
</body>
</html>
```